Packaged Food Business Needs a Packaging Design

We need a package design to be used as a label/sticker on the lids of round and square transparent plastic containers and on the sides of resealable stand-up pouches. The brand name is 'Tastora' - please find attached logo together with pictures of the sample containers and pouch. We will use the packaging to market a wide variety of food categories from nuts, dried fruits, spices, cooking chocolates, baking ingredients, cereals, grains and pulses.

OVERALL FEEDBACK ON DESIGNS ALREADY RECEIVED:

- We have found so far that a lot of our mandatory requirements are not adhered to in designs that have been submitted so far. We would like to emphasise that the ingredient, weight and expiry text will be printed at the time of packing so it should not take prime space on the pack BUT at the same time some 'blank' space needs to flawlessly be incorporated into the overall design for this purpose
- We encourage you to glorify the brand logo in the pack, and absolutely refrain from duplicating the tagline
- Please note that ONE label design will be used to pack a wide variety of food ingredients and therefore please ensure that the choice of your design incorporates this requirement, in the past we have received designs that are limited to only one type of food (like nuts) or have received designs that are too floral or leafy (and not grounded to food
- Please ensure that you submit designs for all three packaging formats, it is critical to see the family look from the on-set

Target Market(s)

The brand is targeting both mothers and professional chefs and therefore the label design should be broadly approachable and convey affordable premium

Industry/Entity Type

Business

Requirements
Must have
• - Consistent with the brand name and logo, the overall look and feel of the packaging should convey values of healthy, gourmet food ingredients, high in nourishment and project a sense of delightful taste
• - The design styling to be modern and 'simplistic' (embracing 'less-is-more' type of a design style)
• - Design a packaging architecture that incorporates the brand logo together with its tagline lock-up of 'savour the goodness in every morsel' - find logo attached
• - The design needs to have a dedicated area to print the ingredient (e.g., Mixed Nuts), weight (e.g., 500g) and expiry (this space needs to be flawlessly incorporated into the design) - this information will be printed either with an inkjet printer or with a rubber stamp so please leave an empty space (the text should not be part of the design, just the area for the text needs to be included in the design)
• - The packaging must include 'Packed By: Kelvane Distributors Ltd, P. O. Box 51946, Kampala - Uganda'
• - For the design of the resealable pouch, please incorporate a window to see through the ingredients and a hole on top to hang on supermarket pegs if necessary
Nice to have
• - We would love to have some design submissions that are bold and cheerful and fun (but not frivolous) - please see attached inspiration for 'fun' packaging. The attachments are purely for inspiration, not to infringe on anyone else's TM and copyrights
• - Incorporate green to convey healthy, organic values
• - Explore use of gold and silver convey premiumness
Should not have
• - Do not duplicate the tagline
• - Do not include the ingredient, weight and expiry in the main graphic of the design, these will be printed at the time of packing so ensure there is provision for this in a flawless way in the design (e.g., via a blank space allocated for this purpose)

```html
<!DOCTYPE html>
<html lang="en">
<head>
<meta charset="utf-8">
<title>Tastora Packaging Labels</title>
<link rel="stylesheet" href="https://fonts.googleapis.com/css2?family=Oswald:wght@400;500;600&family=Bebas+Neue&family=Montserrat:wght@700&display=swap">
<style>
  :root {
    --brown: #40220c;
    --brown-soft: #6b4a38;
    --green: #4c8a2e;
    --window: #5c5c5c;
    --paper: #ffffff;
    --pattern-a: #f3e2cc;
    --pattern-b: #c98d52;
    --label-text: #7a5a46;
  }
  html, body {
    margin: 0;
    padding: 0;
    width: 1200px;
    height: 1200px;
    overflow: hidden;
    background: var(--paper);
  }
  .canvas { position: relative; width: 1200px; height: 1200px; }

  .pattern-fill {
    background: linear-gradient(135deg, var(--pattern-a) 0%, var(--pattern-b) 50%, var(--pattern-a) 100%);
  }

  .brand-name {
    font-family: "Oswald", sans-serif;
    font-weight: 500;
    color: var(--brown);
    text-transform: uppercase;
    text-align: center;
    line-height: 1;
    margin: 0;
  }
  .tagline {
    font-family: "Montserrat", sans-serif;
    font-weight: 700;
    color: var(--green);
    text-transform: uppercase;
    text-align: center;
    margin: 0;
    white-space: nowrap;
  }
  .info-box {
    position: absolute;
    font-family: "Bebas Neue", sans-serif;
    color: var(--label-text);
    box-sizing: border-box;
  }

  /* Round lid label */
  .round-label { position: absolute; left: 111px; top: 90px; width: 400px; height: 400px; }
  .round-label text { font-family: "Bebas Neue", sans-serif; }

  /* Square lid label */
  .square-label {
    position: absolute; left: 58px; top: 548px; width: 469px; height: 303px;
    border: 2px solid var(--brown); box-sizing: border-box; overflow: hidden; background: var(--paper);
  }
  .square-label .band-top { position: absolute; left: 0; top: 0; width: 100%; height: 31px; }
  .square-label .band-bottom { position: absolute; left: 0; top: 222px; width: 100%; height: 65px; }
  .square-label .brand-name { position: absolute; left: 0; width: 100%; top: 100px; font-size: 72px; letter-spacing: 14px; }
  .square-label .tagline { position: absolute; left: 0; width: 100%; top: 190px; font-size: 12px; letter-spacing: 1.5px; }
  .square-label .info-box { top: 239px; width: 127px; height: 41px; background: var(--brown); border-radius: 4px; font-size: 9px; padding: 4px 6px; color: #5e3e2a; }
  .square-label .footer {
    position: absolute; left: 0; bottom: 0; width: 100%; height: 16px; background: var(--brown);
    color: #fff; font-family: "Bebas Neue", sans-serif; font-size: 9px; line-height: 16px; padding-left: 14px; box-sizing: border-box;
  }
  .footer strong { font-weight: 400; font-size: 1.25em; margin-right: 4px; }

  /* Stand-up pouch */
  .pouch {
    position: absolute; left: 599px; top: 208px; width: 571px; height: 857px;
    border: 3px solid var(--brown); box-sizing: border-box; overflow: hidden; background: var(--paper);
  }
  .pouch .band-top { position: absolute; left: 0; top: 0; width: 100%; height: 98px; }
  .pouch .band-middle { position: absolute; left: 0; top: 388px; width: 100%; height: 351px; }
  .pouch .brand-name { position: absolute; left: 0; width: 100%; top: 240px; font-size: 100px; letter-spacing: 20px; }
  .pouch .tagline { position: absolute; left: 0; width: 100%; top: 342px; font-size: 19px; letter-spacing: 2.5px; }
  .pouch .window {
    position: absolute; left: 55px; top: 504px; width: 460px; height: 193px;
    background: var(--window); border: 3px solid var(--brown); border-radius: 14px; box-sizing: border-box;
  }
  .pouch .info-panel { position: absolute; left: 0; top: 739px; width: 100%; height: 118px; background: var(--brown); }
  .pouch .info-box { top: 16px; width: 153px; height: 56px; background: var(--brown-soft); border-radius: 5px; font-size: 18px; padding: 4px 8px; color: #3a1f0c; }
  .pouch .footer {
    position: absolute; left: 14px; top: 88px; color: #fff; font-family: "Bebas Neue", sans-serif; font-size: 14px; white-space: nowrap;
  }
  .pouch .footer strong { font-size: 24px; margin-right: 14px; }
</style>
</head>
<body>
<main class="canvas">

  <svg class="round-label" viewBox="0 0 400 400" aria-label="Round lid label">
    <defs>
      <clipPath id="lid-clip"><circle cx="200" cy="200" r="196"/></clipPath>
      <linearGradient id="lid-pattern" x1="0" y1="0" x2="1" y2="1">
        <stop offset="0" stop-color="#f3e2cc"/>
        <stop offset="0.5" stop-color="#c98d52"/>
        <stop offset="1" stop-color="#f3e2cc"/>
      </linearGradient>
      <path id="lid-arc" d="M 48 300 A 175 175 0 0 0 352 300"/>
    </defs>
    <g clip-path="url(#lid-clip)">
      <rect width="400" height="400" fill="#ffffff"/>
      <rect class="lid-band-top" x="0" y="0" width="400" height="86" fill="url(#lid-pattern)" role="img" aria-label="Pattern of nuts, seeds and leaves"/>
      <rect class="lid-band-bottom" x="0" y="282" width="400" height="118" fill="url(#lid-pattern)" role="img" aria-label="Pattern of nuts, seeds and leaves"/>
      <rect class="lid-best-before" x="109" y="29" width="182" height="37" rx="18" fill="#40220c"/>
      <text x="200" y="42" text-anchor="middle" font-size="9" fill="#7a5a46">BEST BEFORE:</text>
      <rect class="lid-info" x="67" y="303" width="262" height="66" rx="30" fill="#40220c"/>
      <text x="158" y="328" text-anchor="middle" font-size="17" fill="#7a5a46">INGREDIENTS</text>
      <line x1="200" y1="312" x2="200" y2="355" stroke="#7a5a46" stroke-width="1"/>
      <text x="240" y="328" text-anchor="middle" font-size="17" fill="#7a5a46">NET WEIGHT</text>
      <text font-size="9" fill="#40220c"><textPath href="#lid-arc" startOffset="50%" text-anchor="middle">PACKED BY KELVANE DISTRIBUTORS LTD, P. O. BOX 51946, KAMPALA - UGANDA</textPath></text>
    </g>
    <circle cx="200" cy="200" r="196" fill="none" stroke="#40220c" stroke-width="3"/>
    <text x="200" y="245" text-anchor="middle" font-family="Oswald, sans-serif" font-weight="500" font-size="70" letter-spacing="12" fill="#40220c">TASTORA</text>
    <text x="200" y="264" text-anchor="middle" font-family="Montserrat, sans-serif" font-weight="700" font-size="11" letter-spacing="1.4" fill="#4c8a2e">SAVOUR THE GOODNESS IN EVERY MORSEL!</text>
  </svg>

  <section class="square-label" aria-label="Square lid label">
    <div class="band-top pattern-fill" role="img" aria-label="Pattern of nuts, seeds and leaves"></div>
    <h2 class="brand-name">Tastora</h2>
    <p class="tagline">Savour the goodness in every morsel!</p>
    <div class="band-bottom pattern-fill" role="img" aria-label="Pattern of nuts, seeds and leaves"></div>
    <div class="info-box" style="left:17px">INGREDIENTS</div>
    <div class="info-box" style="left:170px">BEST BEFORE</div>
    <div class="info-box" style="left:324px">NET WEIGHT</div>
    <div class="footer"><strong>PACKED BY</strong> KELVANE DISTRIBUTORS LTD, P. O. BOX 51946, KAMPALA - UGANDA</div>
  </section>

  <section class="pouch" aria-label="Stand-up pouch label">
    <div class="band-top pattern-fill" role="img" aria-label="Pattern of nuts, seeds and leaves"></div>
    <h1 class="brand-name">Tastora</h1>
    <p class="tagline">Savour the goodness in every morsel!</p>
    <div class="band-middle pattern-fill" role="img" aria-label="Pattern of nuts, seeds and leaves"></div>
    <div class="window" aria-label="See-through window"></div>
    <div class="info-panel">
      <div class="info-box" style="left:20px">INGREDIENTS</div>
      <div class="info-box" style="left:209px">BEST BEFORE:</div>
      <div class="info-box" style="left:399px">NET WEIGHT</div>
      <div class="footer"><strong>PACKED BY</strong> KELVANE DISTRIBUTORS LTD, P. O. BOX 51946, KAMPALA - UGANDA</div>
    </div>
  </section>

</main>
</body>
</html>
```